Business Card Design - R.T. Custom Cabinets Ltd.

Design a business card, including a new logo for a new company in Vancouver, British Columbia, Canada.

The logo must be available as a separate file.

The card should include all company information including:
R.T. Custom Cabinets Ltd.
2786 Larchmoor Crescent
Burnaby, B.C. V7K 2P9
Telehone: 604-XXX-XXXX
Fax: 604-XXX-XXXX
www.rtcustomcabinets.example

As well as individual contact information for employees:
Name
Position
Telephone
Email

The card must include a thoughtful message as well

Target Market(s)

Custom Cabinets

Industry/Entity Type

Business

Contact Information for Business Card

Important information on the front, thoughtful message on the back

Colors
fbed22
9bcb3c
0355a3
ec1f27

Requirements
Must have
• See project description
Nice to have
• images that showcase custom cabinets (european, modern and traditional) styles

```html
<!DOCTYPE html>
<html lang="en">
<head>
<meta charset="utf-8">
<title>R.T. Custom Cabinets Ltd. – Business Card</title>
<link rel="stylesheet" href="https://fonts.googleapis.com/css2?family=Open+Sans:wght@400;600;700&display=swap">
<style>
  :root {
    --stage: #2b2b2b;
    --card: #121212;
    --ink: #f2f2f2;
    --ink-soft: #d6d6d6;
    --accent-green: #9bcb3c;
    --accent-blue: #0355a3;
    --accent-red: #ec1f27;
    --divider: #2a2a2a;
  }
  * { box-sizing: border-box; margin: 0; padding: 0; }
  html, body { width: 1200px; height: 900px; overflow: hidden; }
  body {
    background: var(--stage);
    font-family: "Open Sans", Arial, sans-serif;
    display: flex;
    align-items: center;
    justify-content: center;
    gap: 60px;
  }
  .card {
    width: 500px;
    height: 290px;
    background: var(--card);
    border-radius: 20px;
    position: relative;
    color: var(--ink);
  }
  /* Front */
  .card-front { display: flex; }
  .brand-mark {
    width: 230px;
    display: flex;
    flex-direction: column;
    align-items: center;
    justify-content: center;
    gap: 14px;
    border-right: 1px solid var(--divider);
    margin: 28px 0;
  }
  .brand-mark .mark-square {
    width: 110px; height: 110px;
    background: var(--accent-green);
  }
  .brand-mark .mark-name {
    font-size: 15px; font-weight: 600; color: var(--ink);
  }
  .contact-block { padding: 34px 0 0 28px; }
  .person-name { color: var(--accent-green); font-size: 19px; font-weight: 700; line-height: 1.1; }
  .person-title { font-size: 12px; color: var(--ink-soft); margin-bottom: 14px; }
  .company-name { font-size: 13px; font-weight: 700; }
  .address { font-size: 13px; color: var(--ink-soft); line-height: 1.45; margin-bottom: 16px; }
  .contact-list { list-style: none; font-size: 13px; line-height: 1.6; }
  .contact-list li { display: flex; align-items: center; gap: 8px; }
  .contact-list svg { width: 11px; height: 11px; fill: var(--accent-green); flex: none; }
  /* Back */
  .card-back {
    display: flex; align-items: center; justify-content: center; gap: 14px;
    box-shadow: 0 4px 0 #0c0c0c, 0 8px 0 #0a0a0a, 0 12px 0 #080808;
  }
  .card-back .mark-square { width: 38px; height: 38px; background: var(--accent-green); }
  .card-back .mark-name { font-size: 20px; font-weight: 600; color: var(--ink); }
</style>
</head>
<body>
  <section class="card card-front" aria-label="Business card front">
    <div class="brand-mark">
      <span class="mark-square"></span>
      <span class="mark-name">R.T. Custom Cabinets</span>
    </div>
    <div class="contact-block">
      <p class="person-name">Daniel Harper</p>
      <p class="person-title">Managing Director</p>
      <p class="company-name">R.T. Custom Cabinets Ltd.</p>
      <p class="address">2786 Larchmoor Crescent<br>Burnaby, B.C. V7K 2P9</p>
      <ul class="contact-list">
        <li><svg viewBox="0 0 16 16"><path d="M3 1l3 3-2 2c1 2 3 4 5 5l2-2 3 3-2 3C6 15 1 10 0 3z"/></svg>604-XXX-XXXX</li>
        <li><svg viewBox="0 0 16 16"><rect x="3" y="1" width="10" height="5"/><rect x="1" y="6" width="14" height="9" rx="1"/></svg>604-XXX-XXXX</li>
        <li><svg viewBox="0 0 16 16"><path d="M0 3h16v10H0z M0 3l8 6 8-6"/></svg>info@rtcustomcabinets.example</li>
        <li><svg viewBox="0 0 16 16"><circle cx="8" cy="8" r="8"/></svg>www.rtcustomcabinets.example</li>
      </ul>
    </div>
  </section>
  <section class="card card-back" aria-label="Business card back">
    <span class="mark-square"></span>
    <span class="mark-name">R.T. Custom Cabinets Ltd.</span>
  </section>
</body>
</html>
```